Business card logo

Hello, I would like a business card for my law firm with a logo composed of my initials "MH". The logo is intended to appear on my business card, my letterhead, envelope and documents from my office. My first and last name (Maren Holt) and "Lawyer" must appear next to the logo. I would like the logo and the characters to be in golden color on a dark background (example black, navy blue). I would especially like a refined work on the logo which should be composed of the letters J and R.

```html
<!DOCTYPE html>
<html lang="en">
<head>
<meta charset="UTF-8">
<title>Maren Holt – Lawyer Business Card</title>
<link href="https://fonts.googleapis.com/css2?family=Montserrat:wght@400;600&display=swap" rel="stylesheet">
<style>
  :root {
    --stage: #1d1d1f;
    --navy: #0c2250;
    --navy-edge: #081a3e;
    --gold: #d8a634;
    --ink-light: #d9dde6;
  }
  * { box-sizing: border-box; margin: 0; padding: 0; }
  html, body { width: 1200px; height: 847px; overflow: hidden; }
  body {
    background: var(--stage);
    display: flex;
    align-items: center;
    justify-content: center;
    gap: 60px;
    font-family: "Montserrat", sans-serif;
  }
  .card {
    position: relative;
    width: 520px;
    height: 300px;
    background: var(--navy);
    border-bottom: 4px solid var(--navy-edge);
    border-radius: 3px;
    box-shadow: 0 18px 40px rgba(0,0,0,.55);
  }

  /* Front */
  .card--front {
    display: flex;
    align-items: center;
    justify-content: center;
  }
  .lockup {
    display: flex;
    flex-direction: column;
    align-items: center;
  }
  .lockup__square {
    width: 44px;
    height: 44px;
    border: 2px solid var(--gold);
    margin-bottom: 14px;
  }
  .lockup__name {
    font-weight: 600;
    font-size: 28px;
    letter-spacing: 1px;
    color: var(--gold);
    text-transform: uppercase;
  }
  .lockup__title {
    display: flex;
    align-items: center;
    gap: 10px;
    margin-top: 8px;
  }
  .lockup__rule {
    width: 70px;
    height: 1px;
    background: var(--ink-light);
  }
  .lockup__role {
    font-size: 11px;
    letter-spacing: 5px;
    color: var(--ink-light);
    text-transform: uppercase;
  }

  /* Back */
  .back__mark {
    position: absolute;
    top: 34px;
    right: 40px;
    display: flex;
    align-items: center;
    gap: 10px;
  }
  .back__square {
    width: 18px;
    height: 18px;
    border: 2px solid var(--gold);
  }
  .back__name {
    font-weight: 600;
    font-size: 16px;
    color: var(--gold);
  }
  .contact {
    position: absolute;
    left: 40px;
    bottom: 30px;
    color: var(--ink-light);
    font-size: 11.5px;
    line-height: 1.55;
  }
  .contact__name {
    font-weight: 600;
    font-size: 17px;
    color: var(--gold);
    text-transform: uppercase;
    line-height: 1.2;
  }
  .contact__role {
    font-size: 13px;
    margin-bottom: 10px;
  }
  .contact__address { margin-bottom: 8px; }
  .contact__line {
    display: flex;
    align-items: center;
    gap: 7px;
  }
  .contact__icon {
    width: 11px;
    height: 11px;
    fill: none;
    stroke: var(--gold);
    stroke-width: 1.6;
  }
</style>
</head>
<body>

  <section class="card card--front">
    <div class="lockup">
      <span class="lockup__square"></span>
      <span class="lockup__name">Maren Holt</span>
      <div class="lockup__title">
        <span class="lockup__rule"></span>
        <span class="lockup__role">Lawyer</span>
        <span class="lockup__rule"></span>
      </div>
    </div>
  </section>

  <section class="card card--back">
    <div class="back__mark">
      <span class="back__square"></span>
      <span class="back__name">Maren Holt</span>
    </div>

    <div class="contact">
      <p class="contact__name">Maren Holt</p>
      <p class="contact__role">Lawyer</p>
      <p class="contact__address">412 Harbor Mill Rd #18<br>Brookfield, CT 06804</p>
      <p class="contact__line">
        <svg class="contact__icon" viewBox="0 0 12 12" aria-hidden="true"><path d="M2 1.5h2.2l1 2.6-1.3 1a6 6 0 0 0 3 3l1-1.3 2.6 1V10a1 1 0 0 1-1 1A8.5 8.5 0 0 1 1 2.5a1 1 0 0 1 1-1z"/></svg>
        203-555-0187
      </p>
      <p class="contact__line">
        <svg class="contact__icon" viewBox="0 0 12 12" aria-hidden="true"><rect x="1" y="2.5" width="10" height="7"/><path d="M1 2.5l5 4 5-4"/></svg>
        office@marenholtlaw.com
      </p>
      <p class="contact__line">
        <svg class="contact__icon" viewBox="0 0 12 12" aria-hidden="true"><circle cx="6" cy="6" r="5"/><path d="M1 6h10M6 1c2.5 2.7 2.5 7.3 0 10M6 1c-2.5 2.7-2.5 7.3 0 10"/></svg>
        www.marenholtlaw.com
      </p>
    </div>
  </section>

</body>
</html>
```